The Deskwell (A new and exciting small Business support solution) Business Cards

The Deskwell Business Card Design

About us:
The Deskwell is a small business support solution, assisting businesses with any marketing, office management and human resource skills.

Objective
To be a small business lifesaver, to relieve busy professionals from mundane operations so they can focus on their businesses future through complete, reliable, efficient and effective client support. To have people say WOW what did we do before The Deskwell.

Industry/Entity Type

Small Business

Colors
0355a3
33a6d7

Requirements
Must have
• Must be similar to the look and feel of my website http://www.thedeskwell-example.com.au/

Must have:

Blue colour is 0094FF

The Logo

A Small Business Support Solution
- Human Resources
- Office Administration
- Marketing

Maribel Torvik
0462 837 105
maribeltorvik@thedeskwell-example.com.au
www.thedeskwell-example.com

```html
<!DOCTYPE html>
<html lang="en">
<head>
<meta charset="utf-8">
<title>The Deskwell – Business Card</title>
<link rel="stylesheet" href="https://fonts.googleapis.com/css2?family=Lato:wght@400;700&display=swap">
<style>
  :root {
    --page-bg: #e6e8eb;
    --card-bg: #ffffff;
    --brand-blue: #3276b8;
    --text-blue: #2c6fb0;
    --ink: #111111;
    --white: #ffffff;
  }
  html, body {
    margin: 0;
    padding: 0;
    width: 1200px;
    height: 970px;
    overflow: hidden;
    background: var(--page-bg);
    font-family: "Lato", Arial, sans-serif;
  }
  .business-card {
    position: absolute;
    left: 100px;
    top: 193px;
    width: 1000px;
    height: 583px;
    background: var(--card-bg);
    overflow: hidden;
    box-shadow: 0 6px 24px rgba(0, 0, 0, 0.18);
  }
  .card-swoosh {
    position: absolute;
    inset: 0;
    width: 1000px;
    height: 583px;
  }
  .holder-name {
    position: absolute;
    right: 64px;
    top: 72px;
    margin: 0;
    font-size: 24px;
    font-weight: 700;
    color: var(--text-blue);
    letter-spacing: 0.3px;
    text-transform: uppercase;
  }
  .brand-name {
    position: absolute;
    left: 68px;
    top: 128px;
    margin: 0;
    font-size: 86px;
    font-weight: 400;
    line-height: 1;
    color: var(--ink);
    letter-spacing: 0.5px;
  }
  .service-list {
    position: absolute;
    left: 68px;
    top: 382px;
    margin: 0;
    padding: 0;
    list-style: none;
  }
  .service-list li {
    display: flex;
    align-items: center;
    height: 35.5px;
    font-size: 21px;
    color: var(--text-blue);
  }
  .service-list .bullet {
    width: 18px;
    height: 18px;
    margin-right: 7px;
    flex: none;
  }
  .contact-list {
    position: absolute;
    right: 64px;
    top: 408px;
    margin: 0;
    padding: 0;
    list-style: none;
    text-align: right;
  }
  .contact-list li {
    display: flex;
    justify-content: flex-end;
    align-items: center;
    height: 36px;
    font-size: 19px;
    color: var(--white);
  }
  .contact-list .contact-icon {
    width: 24px;
    height: 24px;
    margin-left: 9px;
    flex: none;
  }
</style>
</head>
<body>
  <article class="business-card">
    <svg class="card-swoosh" viewBox="0 0 698 407" preserveAspectRatio="none" aria-hidden="true">
      <path d="M0 406 C 225 386 480 272 698 110 L 698 407 L 0 407 Z" fill="#000"/>
      <path d="M8 407 C 228 389 482 290 698 128 L 698 407 Z" fill="#fff"/>
      <path d="M16 407 C 234 391 486 298 698 138 L 698 407 Z" fill="var(--brand-blue)"/>
    </svg>

    <h2 class="holder-name">Maribel Torvik</h2>

    <h1 class="brand-name">The Deskwell</h1>

    <ul class="service-list">
      <li><svg class="bullet" viewBox="0 0 20 20"><g stroke="#000" stroke-width="2.2" stroke-linecap="round"><line x1="10" y1="2" x2="10" y2="18"/><line x1="2" y1="10" x2="18" y2="10"/><line x1="4.3" y1="4.3" x2="15.7" y2="15.7"/><line x1="15.7" y1="4.3" x2="4.3" y2="15.7"/></g></svg>A Small Business Support Solution</li>
      <li><svg class="bullet" viewBox="0 0 20 20"><g stroke="#000" stroke-width="2.2" stroke-linecap="round"><line x1="10" y1="2" x2="10" y2="18"/><line x1="2" y1="10" x2="18" y2="10"/><line x1="4.3" y1="4.3" x2="15.7" y2="15.7"/><line x1="15.7" y1="4.3" x2="4.3" y2="15.7"/></g></svg>Human Resources</li>
      <li><svg class="bullet" viewBox="0 0 20 20"><g stroke="#000" stroke-width="2.2" stroke-linecap="round"><line x1="10" y1="2" x2="10" y2="18"/><line x1="2" y1="10" x2="18" y2="10"/><line x1="4.3" y1="4.3" x2="15.7" y2="15.7"/><line x1="15.7" y1="4.3" x2="4.3" y2="15.7"/></g></svg>Office Administration</li>
      <li><svg class="bullet" viewBox="0 0 20 20"><g stroke="#000" stroke-width="2.2" stroke-linecap="round"><line x1="10" y1="2" x2="10" y2="18"/><line x1="2" y1="10" x2="18" y2="10"/><line x1="4.3" y1="4.3" x2="15.7" y2="15.7"/><line x1="15.7" y1="4.3" x2="4.3" y2="15.7"/></g></svg>Marketing</li>
    </ul>

    <ul class="contact-list">
      <li>0462 837 105
        <svg class="contact-icon" viewBox="0 0 24 24"><rect x="1" y="1" width="22" height="22" rx="4" fill="#fff"/><path d="M8 5 C6 6 5.5 8 6.5 11 C8 15 10.5 17.5 14 19 C16 19.6 17.5 19 18.5 17.5 L16 15 L14 16 C12 15 10 13 9 11 L10.5 9 Z" fill="var(--brand-blue)"/></svg>
      </li>
      <li>maribeltorvik@thedeskwell-example.com.au
        <svg class="contact-icon" viewBox="0 0 24 24"><rect x="2" y="5" width="20" height="14" fill="none" stroke="#fff" stroke-width="2"/><path d="M2 5 L12 13 L22 5 M2 19 L9.5 11 M22 19 L14.5 11" fill="none" stroke="#fff" stroke-width="1.8"/></svg>
      </li>
      <li>www.thedeskwell-example.com
        <svg class="contact-icon" viewBox="0 0 24 24"><g fill="none" stroke="#fff" stroke-width="1.8"><circle cx="12" cy="12" r="9.5"/><ellipse cx="12" cy="12" rx="4" ry="9.5"/><line x1="2.5" y1="12" x2="21.5" y2="12"/><path d="M4.5 7 H19.5 M4.5 17 H19.5"/></g></svg>
      </li>
    </ul>
  </article>
</body>
</html>
```